Full Service Day Spa Needs Wordpress Template Designed

Verdant Spa is a full service day spa, where we make our own line of bath and body products. The current website houses an online store with an TradeNook base (as a WordPress plugin) and simple web pages with information and price lists for services.
For the upgraded website, we are doing a significant makeover and want to include the ability to have full screen video on our main page, windowed or full screen video on feature pages (for example, pages for "Meet our staff" or "Product Demos")
The site should retain standard WordPress compatibility for plugins, such as galleries etc.
The ability to include iframes would be considered a plus so that we can embed external scheduling applications that we subscribe to.
The color scheme for our spa features chocolate brown, taupe, cream, and turquoise for color accents. We would like our website to reflect these colors as our customers find them relaxing.
Our spa has a number of paintings on our walls, which could be used for inspiration for the website design. We like modern abstract art, with curves and swirls. I have included examples of this artwork so that potential designers can see what we like.
The new site must include our logo (provided) and our tag line: "Come Relax With Us" displayed in the upper left in the header.
We would prefer to have the option to put the menu either on the left side, or across the top to the right of the logo.
Words to describe the look we are seeking would be elegant, upscale, relaxing.

Target Market(s)

Our market is primarily local women (in and around our city) who are professionals aged 30 - 65.

Industry/Entity Type

Store

Colors
f78f20
00a990
f37022

Requirements
Must have
• The template should accommodate full screen and partial screen HTML5 video. Must have a menu, could be top or could be side. Should be in shades of browns and neutral colors, with teal accents, or similar highlights to the attached pictures of our artwork we have in the spa. We are looking for a consistent look that our customers can identify is us. Must have our logo in the upper left side of the header.
Nice to have
• Iframes built in would be nice, although we know we can get plugins for that. Likewise we know we can get plugins for the HTML 5 video, we would like the template built with accommodating that in mind. We have seen sites that have full screen video on the main page. We think this looks good.
Should not have
• We are looking for something elegant and upscale, so we are not looking for something "Cartoonish".

```html
<!DOCTYPE html>
<html lang="en">
<head>
<meta charset="utf-8">
<title>Verdant Spa – WordPress Template Layout</title>
<link rel="stylesheet" href="https://fonts.googleapis.com/css2?family=Cormorant+Garamond:ital,wght@0,400;0,500;1,400;1,500&family=PT+Sans:wght@400;700&display=swap">
<style>
  :root {
    --paper: #ffffff;
    --guide: #e0343c;
    --ink: #1c1c1c;
    --note-red: #e0202a;
    --choc-deep: #2a0f0a;
    --choc: #3e1a12;
    --taupe: #6d5548;
    --menu-tan: #d8b883;
    --cream: #e9d8bf;
    --cream-soft: #cdb799;
    --gold: #b89a5c;
    --teal: #2aa8a4;
    --teal-deep: #17706f;
    --serif: "Cormorant Garamond", Georgia, serif;
    --sans: "PT Sans", Arial, sans-serif;
  }
  * { box-sizing: border-box; margin: 0; padding: 0; }
  html, body { width: 1200px; height: 900px; overflow: hidden; background: var(--paper); }
  body { position: relative; font-family: var(--sans); color: var(--ink); }

  .guide { position: absolute; left: 55px; width: 928px; height: 1px; background: var(--guide); }
  .guide-v { position: absolute; top: 18px; width: 1px; height: 848px; background: var(--guide); }

  .site { position: absolute; left: 55px; top: 18px; width: 373px; height: 847px; background: var(--choc); overflow: hidden; }

  .header { position: absolute; left: 0; top: 0; width: 373px; height: 63px;
    background: linear-gradient(90deg, #2c0f0b, #4a1d15 50%, #2c0f0b); }
  .brand-dot { position: absolute; left: 18px; top: 16px; width: 30px; height: 30px; border-radius: 50%; background: var(--cream-soft); }
  .brand-name { position: absolute; left: 64px; top: 17px; font-family: var(--serif); font-style: italic; font-size: 24px; color: var(--cream); }
  .header-phone { position: absolute; right: 18px; top: 26px; font-family: var(--serif); font-style: italic; font-size: 16px; color: var(--cream); }

  .hero { position: absolute; left: 0; top: 63px; width: 373px; height: 171px;
    background: linear-gradient(160deg, #3a1a12 0%, #c98a6c 22%, #e9bca0 45%, #d59a7c 62%, #6a2e1e 82%, #2a120c 100%); }

  .menu { position: absolute; left: 0; top: 234px; width: 373px; height: 16px; display: flex; background: var(--taupe); }
  .menu a { display: block; height: 16px; border-right: 1px solid #c9b8a8; font-family: var(--serif); font-style: italic;
    font-size: 10.5px; line-height: 16px; color: var(--cream); text-decoration: none; text-align: center; }
  .menu a.current { background: var(--menu-tan); color: #4a2a1a; }

  .panel { position: absolute; left: 0; width: 373px;
    background: radial-gradient(ellipse at 50% 40%, #4c2117, var(--choc) 55%, var(--choc-deep) 100%); }
  .intro { top: 250px; height: 254px; }
  .deals { top: 504px; height: 275px; border-top: 1px solid #1a0805; }

  .panel-title { position: absolute; left: 0; width: 100%; text-align: center; font-family: var(--serif); font-style: italic;
    font-weight: 400; font-size: 25px; color: var(--cream-soft); }
  .lede { position: absolute; left: 40px; width: 293px; text-align: center; font-family: var(--serif); font-style: italic;
    font-size: 6px; line-height: 8.5px; color: var(--cream); }

  .tile { position: absolute; width: 100px; text-align: center; }
  .tile-photo { display: block; margin: 0 auto; width: 64px; height: 64px; border-radius: 50%;
    border: 2px solid var(--gold); box-shadow: 0 0 0 2px #2a0f0a; }
  .tile-label { font-family: var(--serif); font-style: italic; font-size: 12px; color: var(--cream-soft); margin-top: 10px; }
  .tile-text { font-family: var(--serif); font-style: italic; font-size: 6px; line-height: 8.5px; color: var(--cream); width: 62px; margin: 6px auto 0; }
  .tile-badge { display: inline-block; margin-top: 11px; padding: 5px 9px; border: 1px solid var(--gold); border-radius: 10px;
    font-family: var(--serif); font-style: italic; font-size: 13px; line-height: 14px; color: var(--cream); }

  .footer { position: absolute; left: 0; top: 779px; width: 373px; height: 46px; background: #2e120c; }
  .footer-address { position: absolute; left: 24px; top: 15px; font-size: 5.5px; line-height: 7px; color: #b7a392; }
  .social { position: absolute; top: 24px; width: 10px; height: 10px; border-radius: 2px; background: #8f7a6c; }
  .footer-phone { position: absolute; right: 22px; top: 22px; font-family: var(--serif); font-style: italic; font-size: 14px; color: var(--cream); }

  .legal { position: absolute; left: 0; top: 825px; width: 373px; height: 22px; background: #200a07;
    font-size: 4.5px; line-height: 22px; text-align: center; color: #cdbfb2; }

  .annotation { position: absolute; left: 471px; font-size: 12px; line-height: 15px; color: var(--ink); }

  .notes { position: absolute; left: 995px; width: 180px; }
  .notes-title { position: absolute; left: 2px; top: 24px; font-size: 40px; font-weight: 400; color: var(--ink); }
  .notes-body { position: absolute; left: 0; top: 97px; width: 166px; font-size: 11px; line-height: 14.5px; }
  .notes-body p + p { margin-top: 14.5px; }
  .notes-alert { position: absolute; left: 0; top: 333px; width: 170px; font-size: 11px; line-height: 14.5px; font-weight: 700; color: var(--note-red); }
</style>
</head>
<body>

  <div class="guide" style="top:18px"></div>
  <div class="guide" style="top:80px"></div>
  <div class="guide" style="top:251px"></div>
  <div class="guide" style="top:268px"></div>
  <div class="guide" style="top:522px"></div>
  <div class="guide" style="top:797px"></div>
  <div class="guide" style="top:842px"></div>
  <div class="guide" style="top:865px"></div>
  <div class="guide-v" style="left:983px"></div>

  <main class="site">
    <header class="header">
      <span class="brand-dot"></span>
      <span class="brand-name">Verdant Spa</span>
      <span class="header-phone">Call: 987654321</span>
    </header>

    <div class="hero" role="img" aria-label="Header photo of a woman receiving a relaxing back massage"></div>

    <nav class="menu">
      <a href="#" style="width:55px">Home</a>
      <a href="#" class="current" style="width:60px">Shop</a>
      <a href="#" style="width:75px">Services</a>
      <a href="#" style="width:55px">Contact</a>
      <a href="#" style="width:67px">Price List</a>
      <a href="#" style="width:61px;border-right:0">About</a>
    </nav>

    <section class="panel intro">
      <h2 class="panel-title" style="top:37px">Come Relax With Us</h2>
      <p class="lede" style="top:83px">It is a long established fact that a reader will be distracted by the readable content of a page when looking at its layout. The point of using Lorem Ipsum is that it has a more-or-less normal distribution of letters, as opposed to using 'Content here, content here'.</p>

      <a class="tile" style="left:15px;top:120px">
        <span class="tile-photo" role="img" aria-label="Photo of a manicure" style="background:linear-gradient(135deg,#6a3a28,#d9a98a 45%,#f0d4bf 60%,#8a5a44)"></span>
        <div class="tile-label">Nail</div>
        <div class="tile-text">It is a long established fact that a reader will be distracted.</div>
      </a>
      <a class="tile" style="left:130px;top:120px">
        <span class="tile-photo" role="img" aria-label="Photo of a facial massage" style="background:linear-gradient(135deg,#f7eee6,#e6c4ac 45%,#c99a80 70%,#8a6a5a)"></span>
        <div class="tile-label">Massage</div>
        <div class="tile-text">It is a long established fact that a reader will be distracted.</div>
      </a>
      <a class="tile" style="left:245px;top:120px">
        <span class="tile-photo" role="img" aria-label="Photo of candles, flowers and spa stones" style="background:linear-gradient(160deg,#2a120c,#8a3a28 40%,#e0a090 60%,#5a2418)"></span>
        <div class="tile-label">Theraphy</div>
        <div class="tile-text">It is a long established fact that a reader will be distracted.</div>
      </a>
    </section>

    <section class="panel deals">
      <h2 class="panel-title" style="top:34px">Best Deals for Members</h2>

      <a class="tile" style="left:17px;top:82px">
        <span class="tile-photo" role="img" aria-label="Photo of a flower and a hand treatment" style="background:linear-gradient(135deg,#fbf6f0,#eed8c8 50%,#c99a88)"></span>
        <div class="tile-badge">On Sale</div>
        <div class="tile-text">It is a long established fact that a reader will be distracted.</div>
      </a>
      <a class="tile" style="left:132px;top:82px">
        <span class="tile-photo" role="img" aria-label="Gold coin image for rewards" style="background:radial-gradient(circle at 40% 35%,#f6e39a,#c9a040 55%,#7a5a1a)"></span>
        <div class="tile-badge">Rewards</div>
        <div class="tile-text">It is a long established fact that a reader will be distracted.</div>
      </a>
      <a class="tile" style="left:248px;top:82px">
        <span class="tile-photo" role="img" aria-label="Photo of turquoise beaded bracelets" style="background:linear-gradient(135deg,#efe6dc,var(--teal) 40%,#3a2418 62%,var(--teal-deep))"></span>
        <div class="tile-badge">Specials</div>
        <div class="tile-text">It is a long established fact that a reader will be distracted.</div>
      </a>

      <p class="lede" style="top:244px">It is a long established fact that a reader will be distracted by the readable content of a page when looking at its layout. The point of using Lorem Ipsum is that it has a more-or-less normal distribution of letters, as opposed to using 'Content here, content here'.</p>
    </section>

    <footer class="footer">
      <div class="footer-address">Verdant Spa<br>48-2210 Linden Ave<br>Riverton, SK</div>
      <span class="social" style="left:127px"></span>
      <span class="social" style="left:168px"></span>
      <span class="social" style="left:208px"></span>
      <span class="footer-phone">Call: 987654321</span>
    </footer>
    <div class="legal">Terms of Use | Privacy Policy | Sitemap &nbsp; © Copyright 2014 · Verdant Spa</div>
  </main>

  <p class="annotation" style="top:30px;width:480px">The logo and telephones section is dynamic</p>
  <p class="annotation" style="top:163px;width:345px">This section can be anything which you like to place, example video header / static image or a slider.</p>
  <p class="annotation" style="top:252px;width:480px">Menu here is also dynamic</p>
  <p class="annotation" style="top:322px;width:445px">This is a first section of the introduction on the home page. The images in circle are also buttons which takes to the various pages of your business highlights.</p>
  <p class="annotation" style="top:646px;width:462px">I have also added additional section here which will then can be any other highlights points of your choice. In this case, I have suggested to have a members section and other special deals which you would like to promote.</p>
  <p class="annotation" style="top:797px;width:462px">This&nbsp; footer section is also dynamic, which means you can change your address line, social media links, or any other information which you might like to have. You may also like to add in your categories or site mape infor here</p>
  <p class="annotation" style="top:847px;width:480px">This section pf the template is fixed,</p>

  <aside class="notes">
    <h2 class="notes-title">Note:</h2>
    <div class="notes-body">
      <p>This is a wordpress template, a unique theme that's created for Verdant Spa.</p>
      <p>Th letters and buttons are coded in CSS which means you will be able to update them in your website as per you normally do, the only difference is the look and feel will be as what you see here in the visual.</p>
    </div>
    <p class="notes-alert">The rounded images will be coded and will appear as you see here. However, these images can be changed to your liking in your wordpress site. They are just button links to your assigned pages.</p>
  </aside>

</body>
</html>
```